Plumbing business card and logo desgin

Need a new business card and logo for a plumbing business based in Warragul, Australia. Business name is 7Kelby plumbing & air-conditioning. We service all plumbing and gasfitting needs and installation of air-conditioning. We clear blocked drains, install new hot water systems, central heating, new and existing homes, roofing, sanitary and drainage.
i would like to have a space on there for website, email, phone, licence number and what we do as a company.
i would like a water droplet to be incorporated into the design to try and stand out that we are a plumbing business

Contact Information for Business Card

website:
phone number: 0458271936
Licence Number: 382716

Logo Text

7Kelby Plumbing & Air-Conditioning

```html
<!DOCTYPE html>
<html lang="en">
<head>
<meta charset="utf-8">
<title>7Kelby Plumbing &amp; Air-Conditioning – Business Card</title>
<link href="https://fonts.googleapis.com/css2?family=Poppins:wght@400;500;600&display=swap" rel="stylesheet">
<style>
  :root {
    --navy: #1b1aa0;
    --navy-deep: #12128a;
    --navy-light: #3434c0;
    --cyan: #22d3e6;
    --white: #ffffff;
    --paper: #f5f6f8;
    --backdrop: #e4e6ea;
  }
  * { box-sizing: border-box; margin: 0; padding: 0; }
  html, body { width: 1200px; height: 780px; overflow: hidden; }
  body {
    background: var(--backdrop);
    font-family: "Poppins", sans-serif;
    display: flex;
    flex-direction: column;
    align-items: center;
    justify-content: center;
    gap: 40px;
  }
  .card {
    position: relative;
    width: 560px;
    height: 320px;
    border-radius: 18px;
    background: var(--paper);
    overflow: hidden;
    box-shadow: 0 6px 18px rgba(0,0,0,0.15);
  }
  .card-front .band {
    position: absolute;
    left: 0; top: 0;
    width: 560px; height: 320px;
  }
  .brand {
    position: absolute;
    display: flex;
    align-items: center;
    gap: 12px;
    color: var(--navy);
    font-weight: 600;
  }
  .brand-dot {
    flex: none;
    border-radius: 50%;
    background: var(--navy);
  }
  .card-front .brand {
    right: 40px; top: 40px;
    font-size: 17px;
    line-height: 1.3;
    max-width: 300px;
  }
  .card-front .brand-dot { width: 30px; height: 30px; }
  .identity {
    position: absolute;
    left: 40px; top: 190px;
    color: var(--white);
  }
  .identity .person-name { font-size: 26px; font-weight: 500; line-height: 1.1; }
  .identity .person-role { font-size: 15px; font-weight: 400; margin-top: 2px; }
  .identity .rule { width: 70px; height: 2px; background: var(--white); margin-top: 16px; }
  .contact-list {
    position: absolute;
    left: 250px; top: 176px;
    list-style: none;
    color: var(--white);
    font-size: 14px;
    line-height: 1.55;
  }
  .contact-list li { display: flex; align-items: center; gap: 10px; }
  .contact-list svg { width: 14px; height: 14px; flex: none; }
  .contact-list .licence { margin-top: 6px; padding-left: 24px; }
  .card-back { display: flex; align-items: center; justify-content: center; }
  .card-back .brand { position: static; font-size: 24px; gap: 16px; max-width: 420px; line-height: 1.3; }
  .card-back .brand-dot { width: 44px; height: 44px; }
</style>
</head>
<body>

<section class="card card-front">
  <svg class="band" viewBox="0 0 560 320" aria-hidden="true">
    <defs>
      <linearGradient id="bandFill" x1="0" y1="0" x2="1" y2="1">
        <stop offset="0" stop-color="#12128a"/>
        <stop offset="0.5" stop-color="#3434c0"/>
        <stop offset="1" stop-color="#1b1aa0"/>
      </linearGradient>
    </defs>
    <path d="M0 118 Q280 178 560 150 L560 320 L0 320 Z" fill="url(#bandFill)"/>
    <path d="M0 118 Q280 178 560 150" fill="none" stroke="#22d3e6" stroke-width="3"/>
  </svg>

  <div class="brand">
    <span class="brand-dot"></span>
    <span class="brand-name">7Kelby Plumbing &amp; Air-Conditioning</span>
  </div>

  <div class="identity">
    <p class="person-name">Liam Carter</p>
    <p class="person-role">Director</p>
    <div class="rule"></div>
  </div>

  <ul class="contact-list">
    <li>
      <svg viewBox="0 0 24 24"><path fill="#fff" d="M6.6 10.8a15 15 0 006.6 6.6l2.2-2.2a1 1 0 011-.25 11.4 11.4 0 003.6.57 1 1 0 011 1V20a1 1 0 01-1 1A17 17 0 013 4a1 1 0 011-1h3.5a1 1 0 011 1 11.4 11.4 0 00.57 3.6 1 1 0 01-.25 1z"/></svg>
      0458271936
    </li>
    <li>
      <svg viewBox="0 0 24 24"><path fill="#fff" d="M2 5h20v14H2z"/><path fill="none" stroke="#1b1aa0" stroke-width="1.6" d="M2 5l10 8 10-8"/></svg>
      hello@kelbymail.com
    </li>
    <li>
      <svg viewBox="0 0 24 24"><circle cx="12" cy="12" r="10" fill="none" stroke="#fff" stroke-width="2"/><path fill="none" stroke="#fff" stroke-width="1.6" d="M2 12h20M12 2c3 3 3 17 0 20M12 2c-3 3-3 17 0 20"/></svg>
      www.kelbyplumbing.com.au
    </li>
    <li class="licence">Licence Number: 382716</li>
  </ul>
</section>

<section class="card card-back">
  <div class="brand">
    <span class="brand-dot"></span>
    <span class="brand-name">7Kelby Plumbing &amp; Air-Conditioning</span>
  </div>
</section>

</body>
</html>
```